Wedding Save the Date Design Image

I updated the brief with an additional image that used more negative white space and is a bit more "watercolor" in nature. We are going to have our wedding in Lake Como, Italy, and we need to send out a simple "save the date" invite with a key image that captures the fun and vibe of Lake Como. We are thinknig about mabye an iconic part of Lake Como as the inspiration image... maybe the classib boats on the lake, or some version of Casa Lunetti where we will have the wedding... but the idea is just to create an image that conveys the "essence" or fun/"Italian" vibe of Lake Como to get people excited. Perhaps a "watercolor" style image or other expressive artwork... Definitely not a photo or direct image... this should be more whimsical and "expressive" in artistic tone.

```html
<!DOCTYPE html>
<html lang="en">
<head>
<meta charset="utf-8">
<title>Save the Date – Lake Como</title>
<link rel="stylesheet" href="https://fonts.googleapis.com/css2?family=Tinos:wght@400;700&family=Great+Vibes&display=swap">
<style>
  :root {
    --backdrop: #e4e3e6;
    --card: #ffffff;
    --ink: #3a3a3a;
    --ink-soft: #4a4a4a;
    --rule: #555555;
  }
  * { margin: 0; padding: 0; box-sizing: border-box; }
  html, body { width: 1040px; height: 1200px; overflow: hidden; background: var(--backdrop); }
  .canvas { position: relative; width: 1040px; height: 1200px; }
  .card {
    position: absolute; left: 92px; top: 0;
    width: 856px; height: 1200px;
    background: var(--card);
    overflow: hidden;
  }
  .meta {
    position: absolute; top: 48px;
    font-family: "Tinos", "Times New Roman", serif;
    font-weight: 700; font-size: 25px; color: var(--ink);
  }
  .meta--place { left: 81px; }
  .meta--date { right: 62px; }
  .artwork { position: absolute; left: 96px; top: 96px; width: 704px; height: 936px; }
  .headline {
    position: absolute; left: 229px; width: 442px; top: 190px;
    text-align: center; font-family: "Tinos", "Times New Roman", serif; color: var(--ink);
  }
  .headline__small { font-size: 39px; line-height: 46px; letter-spacing: 0.5px; }
  .headline__rule { height: 1px; background: var(--rule); }
  .headline__big {
    font-size: 100px; line-height: 84px; letter-spacing: 30px;
    padding-left: 30px; padding-top: 2px;
  }
  .couple {
    position: absolute; left: 0; width: 856px; top: 1020px;
    text-align: center; font-family: "Great Vibes", cursive;
    font-size: 62px; color: var(--ink-soft);
  }
</style>
</head>
<body>
<div class="canvas">
  <div class="card">
    <div class="meta meta--place">NY, NY</div>
    <div class="meta meta--date">DEC, 2025</div>

    <svg class="artwork" viewBox="0 0 704 936" role="img" aria-label="Watercolour painting of a Lake Como village with terracotta villas, cypress trees, misty mountains and classic wooden boats moored on turquoise water">
      <defs>
        <linearGradient id="sceneTones" x1="0.25" y1="0" x2="0.55" y2="1">
          <stop offset="0" stop-color="#cdc7cc"/>
          <stop offset="0.18" stop-color="#b4aeb1"/>
          <stop offset="0.3" stop-color="#c6ced1"/>
          <stop offset="0.42" stop-color="#dcae93"/>
          <stop offset="0.54" stop-color="#c99a7f"/>
          <stop offset="0.64" stop-color="#86bfc5"/>
          <stop offset="0.82" stop-color="#5eaab6"/>
          <stop offset="1" stop-color="#d4ebee"/>
        </linearGradient>
        <filter id="washEdge" x="-10%" y="-10%" width="120%" height="120%">
          <feTurbulence type="fractalNoise" baseFrequency="0.018" numOctaves="3" seed="7" result="noise"/>
          <feDisplacementMap in="SourceGraphic" in2="noise" scale="60" xChannelSelector="R" yChannelSelector="G" result="ragged"/>
          <feGaussianBlur in="ragged" stdDeviation="7"/>
        </filter>
      </defs>
      <path filter="url(#washEdge)" fill="url(#sceneTones)" opacity="0.88"
        d="M70 90 C170 40 300 30 420 45 C540 55 640 80 690 150 L694 520 C696 660 676 780 630 870 C550 915 390 925 260 910 C150 895 80 860 60 770 C36 620 20 440 30 280 C36 190 40 130 70 90 Z"/>
    </svg>

    <div class="headline">
      <div class="headline__small">SAVE THE</div>
      <div class="headline__rule"></div>
      <div class="headline__big">DATE</div>
      <div class="headline__rule"></div>
    </div>

    <div class="couple">Lorenzo and Adrian</div>
  </div>
</div>
</body>
</html>
```